Launching a consulting business

I need a business card to launch a new consulting business. I provide executive level consultation throughout New York state to CEO and ED's who run and manage non-fo-profit corporations who support individuals with intellectual and developmental disabilities. The field is undergoing an evolution from a social model of care to more outcome based strategies. Having expertise in health care, leading a $50M business providing this service and working in the government creating policy I can bring to the Executive and corporations compassion, vision, strategy with a clear understanding of business practices for success. The field is moving to managed care. My background in health care management brings the expertise to create opportunities and possibilities. I currently have three projects I am consulting on - 1. Field expert assisting an accounting firm in the creation of a managed care application to become a managed care company supporting the ID/DD field. I crafted the care management model 2. Strategizing on product line creation to assure an agency is ready with a compendium services supporting the ID/DD field. 3. Facilitating a financial model to assist in predicting costs to render services in ID/DD. Developing and overlaying outcome measures to position agencies for effective marketing.
Quality is my passion and assuring all people live their life's dreams.
I would also like a template for letterhead stationary following what is created with my business card.
I wold like to incorporate a cranberry/sage tartan plaid within the design.

Please note my last name is spelled wrong on the attachment. I also do not want the tartan plaid used covering the entire card. i open to other ideas and suggestions.

Industry/Entity Type

Government

Contact Information for Business Card

Denise M Forbush
Phone - 845-562-7183
Cell phone 845-734-2096
Email address - denisemfor@quillpost.com

```html
<!DOCTYPE html>
<html lang="en">
<head>
<meta charset="utf-8">
<title>Denise M Forbush – Business Cards</title>
<link rel="stylesheet" href="https://fonts.googleapis.com/css2?family=EB+Garamond:wght@400;500&family=Questrial&display=swap">
<style>
  :root {
    --backdrop: #e4e4e2;
    --pine: #0f5a4d;
    --pine-deep: #0a3d35;
    --pine-glow: #1f6b5e;
    --paper: #ffffff;
    --ink-green: #0e5347;
    --text-light: #e2ece9;
    --text-soft: #b9cfca;
  }
  * { margin: 0; padding: 0; box-sizing: border-box; }
  html, body {
    width: 1200px; height: 871px; overflow: hidden;
    background: var(--backdrop);
  }
  .stage {
    position: relative; width: 1200px; height: 871px;
    display: flex; align-items: center; justify-content: center; gap: 40px;
  }
  .card {
    position: relative; width: 520px; height: 297px; overflow: hidden;
    box-shadow: 0 10px 24px rgba(0,0,0,.25);
  }

  /* Front */
  .card-front { background: var(--pine-deep); }
  .front-visual {
    position: absolute; inset: 0;
    background:
      radial-gradient(ellipse 55% 60% at 52% 48%, rgba(80,130,120,.55), rgba(20,70,60,0) 70%),
      linear-gradient(135deg, var(--pine-glow) 0%, var(--pine-deep) 55%, #072e28 100%);
  }
  .front-name {
    position: absolute; left: 0; right: 0; top: 112px; text-align: center;
    font-family: "EB Garamond", Georgia, serif; font-weight: 400;
    font-size: 42px; letter-spacing: 1.5px; color: var(--text-light);
  }
  .front-title {
    position: absolute; left: 0; right: 0; top: 166px; text-align: center;
    padding-left: 40px;
    font-family: "Questrial", "Century Gothic", sans-serif;
    font-size: 13px; letter-spacing: .8px; color: var(--text-soft);
  }

  /* Back */
  .card-back { background: var(--paper); }
  .back-art { position: absolute; inset: 0; }
  .back-name {
    position: absolute; left: 28px; top: 78px;
    font-family: "EB Garamond", Georgia, serif; font-weight: 500;
    font-size: 25px; letter-spacing: 1px; color: var(--ink-green);
  }
  .back-title {
    position: absolute; left: 28px; top: 146px;
    font-family: "Questrial", "Century Gothic", sans-serif;
    font-size: 14.5px; letter-spacing: .9px; color: var(--ink-green);
    white-space: nowrap;
  }
  .contact-list {
    position: absolute; left: 262px; top: 196px; list-style: none;
    font-family: "Questrial", "Century Gothic", sans-serif;
    font-size: 14px; letter-spacing: 1px; color: var(--text-soft);
  }
  .contact-list li { display: flex; align-items: center; height: 25px; white-space: nowrap; }
  .contact-list svg { width: 16px; height: 16px; margin-right: 16px; flex: none; }
</style>
</head>
<body>
<main class="stage">

  <section class="card card-front">
    <div class="front-visual" role="img" aria-label="Soft dark green photograph of hands joining puzzle pieces"></div>
    <h1 class="front-name">Denise M Forbush</h1>
    <p class="front-title">Executive Business Strategy Consultant</p>
  </section>

  <section class="card card-back">
    <svg class="back-art" viewBox="0 0 520 297" width="520" height="297" aria-hidden="true">
      <defs>
        <linearGradient id="panelShade" x1="0" y1="0" x2="1" y2="1">
          <stop offset="0" stop-color="#146354"/>
          <stop offset="1" stop-color="#0b453c"/>
        </linearGradient>
        <filter id="ribbonShadow" x="-5%" y="-30%" width="115%" height="180%">
          <feDropShadow dx="1" dy="2" stdDeviation="1.5" flood-color="#000" flood-opacity=".35"/>
        </filter>
      </defs>
      <rect x="244" y="0" width="276" height="297" fill="url(#panelShade)"/>
      <polygon points="236,140 384,140 366,165 236,165" fill="var(--paper)" filter="url(#ribbonShadow)"/>
      <rect x="200" y="138" width="44" height="30" fill="var(--paper)"/>
    </svg>

    <h2 class="back-name">Denise M Forbush</h2>
    <p class="back-title">Executive Business Strategy Consultant</p>

    <ul class="contact-list">
      <li>
        <svg viewBox="0 0 16 16" fill="none" stroke="currentColor" stroke-width="1.3"><rect x="4.5" y="1.5" width="7" height="13" rx="1.2"/><line x1="7" y1="12.3" x2="9" y2="12.3"/></svg>
        845-734-2096
      </li>
      <li>
        <svg viewBox="0 0 16 16" fill="none" stroke="currentColor" stroke-width="1.3"><path d="M2 6c0-2 3-3 6-3s6 1 6 3l-2.5 1L10 5.5H6L4.5 7z"/><rect x="3.5" y="8" width="9" height="5.5" rx="1"/><circle cx="8" cy="10.7" r="1.4"/></svg>
        845-562-7183
      </li>
      <li>
        <svg viewBox="0 0 16 16" fill="none" stroke="currentColor" stroke-width="1.3"><rect x="1.5" y="3.5" width="13" height="9"/><polyline points="1.5,3.5 8,9 14.5,3.5"/></svg>
        denisemfor@quillpost.com
      </li>
    </ul>
  </section>

</main>
</body>
</html>
```